Redesign of an educational Eye website for Medical Students and Healthcare professionals

www.corvantisportal.com is an educational resource, illustrated using high quality 3D animations, for undergraduate medical students and healthcare professionals to learn about the anatomy of the human eye and associated common eye disorders.

The website was originally developed (using a Joomla template) a couple of years ago and we now want to update the brand and design of the site. Example content and animations can be found at https://www.corvantisportal.com/overview or https://www.corvantisportal.com/ocular-anatomy/orbital-anatomy

We would like a new logo and home page design (to include new colour palette, fonts and updated overall design).

The attached PowerPoint contains an example layout of the revised components we want to appear on the new Home page. We plan to have a hero panel at the top of page playing a short video of some of the animations. Similar to how this site works (www.zembri.uk.com).

We want the new site to feel Professional, Modern and Clean and simple.

Target Market(s)

Undergraduate medical students and Healthcare Professionals

Industry/Entity Type

Medical

Logo Text

Corvantis Portal

Number of Pages Required

1 page

Font styles to use
Sans Serif

Colors

Designer to choose colors to be used in the design.

```html
<!DOCTYPE html>
<html lang="en">
<head>
<meta charset="utf-8">
<title>Corvantis Portal</title>
<link href="https://fonts.googleapis.com/css2?family=Open+Sans:wght@300;400;600;700&display=swap" rel="stylesheet">
<style>
:root{
  --blue:#2b9be8;
  --blue-dark:#1f86cf;
  --green:#2bbf6a;
  --ink:#333a40;
  --muted:#7a7f84;
  --soft:#f2f2f2;
  --team-bg:#d4d4d4;
  --line:#dcdcdc;
  --white:#ffffff;
}
*{box-sizing:border-box;margin:0;padding:0}
html,body{width:1200px;height:3888px;overflow:hidden}
body{font-family:'Open Sans',Arial,sans-serif;color:var(--ink);background:var(--white);position:relative}
section,header,footer{position:absolute;left:0;width:1200px}
.abs{position:absolute}

/* header */
.site-header{top:0;height:143px}
.brand{left:117px;top:38px;display:flex;align-items:center;gap:14px}
.brand-mark{width:44px;height:44px;border-radius:50%;border:5px solid var(--blue)}
.brand-name{font-size:38px;font-weight:400;color:var(--blue);letter-spacing:.5px}
.sign-in{right:100px;top:56px;font-size:22px;color:var(--blue);display:flex;align-items:center;gap:10px}

/* hero */
.hero{top:143px;height:557px;background:radial-gradient(ellipse at 50% 40%,#5a5450 0%,#3a3532 45%,#1d1a19 100%);text-align:center;color:var(--white)}
.hero-play{left:553px;top:90px;width:94px;height:94px}
.hero-title{top:268px;width:100%;font-size:64px;font-weight:300}
.hero-text{top:350px;left:290px;width:620px;font-size:17px;line-height:24px;color:#e6e6e6}
.hero-actions{top:432px;width:100%;display:flex;justify-content:center;gap:22px}
.btn{display:inline-block;font-size:14px;font-weight:700;color:var(--white);padding:14px 18px;border-radius:4px;text-transform:uppercase}
.btn-blue{background:var(--blue)}
.btn-green{background:var(--green)}

/* trusted */
.trusted{top:700px;height:251px}
.trusted-title{top:31px;width:100%;text-align:center;font-size:18px;color:#555}
.trusted-rule{top:44px;height:1px;background:var(--line);width:430px}
.partner-row{top:78px;left:34px;display:flex;gap:19px}
.partner{width:164px;height:129px;border:1px solid var(--line);display:flex;align-items:center;justify-content:center}
.partner span{width:86px;height:86px;border-radius:50%;background:#cfcfcf}

/* why */
.why{top:951px;height:643px;background:var(--soft)}
.section-title{width:100%;text-align:center;font-size:31px;font-weight:400;color:var(--ink)}
.why .section-title{top:28px}
.feature h3{font-size:24px;font-weight:600;margin-bottom:14px}
.feature p{font-size:14px;color:var(--muted);line-height:22px;margin-bottom:14px}
.feature li{font-size:14px;color:var(--muted);line-height:26px;list-style:none}
.feature li::before{content:"– ";}
.feature-credible{left:176px;top:150px;width:420px}
.feature-visual{left:661px;top:420px;width:420px}
.photo-eye{left:720px;top:94px;width:247px;height:238px;background:linear-gradient(135deg,#7a4e36,#3e2418)}
.photo-drops{left:233px;top:366px;width:247px;height:243px;background:linear-gradient(135deg,#c99a86,#5d7d80)}

/* modules */
.modules{top:1594px;height:575px}
.modules .section-title{top:30px}
.module{top:109px;width:337px;height:409px;background:var(--white);box-shadow:0 1px 4px rgba(0,0,0,.12)}
.module-img{height:207px}
.module-body{padding:22px 28px}
.module h4{font-size:17px;font-weight:600;margin-bottom:22px}
.module p{font-size:13px;color:var(--muted);line-height:20px;height:82px}
.read-more{font-size:12px;font-weight:700;color:var(--ink)}
.m1{left:80px}.m2{left:443px}.m3{left:806px}
.m1 .module-img{background:linear-gradient(135deg,#8a4a32,#1e1e1e)}
.m2 .module-img{background:linear-gradient(135deg,#c26a58,#5a6c70)}
.m3 .module-img{background:linear-gradient(135deg,#b07e66,#4a3226)}

/* team */
.team{top:2169px;height:617px;background:var(--team-bg)}
.team .section-title{top:30px}
.member{top:99px;width:292px;height:384px;background:var(--white);text-align:center}
.member-photo{margin:10px;height:270px;background:linear-gradient(180deg,#e7e9ec,#c9ccd2)}
.member h4{font-size:21px;font-weight:400;margin-top:16px;letter-spacing:.5px}
.member p{font-size:14px;color:var(--muted);margin-top:6px}
.t1{left:135px}.t2{left:459px}.t3{left:780px}

/* testimonial */
.testimonials{top:2786px;height:420px}
.testimonials .section-title{top:40px}
.quote-photo{left:117px;top:125px;width:303px;height:215px;background:linear-gradient(135deg,#8c7062,#2e2a28)}
.quote{left:461px;top:125px;width:640px}
.quote h4{font-size:21px;font-weight:600;color:var(--blue)}
.quote h5{font-size:17px;font-weight:600;color:#555;margin-top:14px;line-height:24px}
.quote p{font-size:13px;color:var(--muted);line-height:21px;margin-top:14px}
.dots{top:370px;width:100%;display:flex;justify-content:center;gap:10px}
.dots span{width:8px;height:8px;border-radius:50%;background:#bbb}
.dots span.on{background:#333}

/* cta */
.cta{top:3206px;height:249px;background:var(--blue);text-align:center;color:var(--white)}
.cta h2{margin-top:62px;font-size:28px;font-weight:700}
.cta p{margin-top:8px;font-size:18px;font-weight:600}
.cta .btn-ghost{display:inline-block;margin-top:30px;background:var(--white);color:var(--ink);font-size:13px;padding:10px 22px;border-radius:20px}

/* charity */
.charity{top:3455px;height:207px;text-align:center}
.charity h2{margin-top:36px;font-size:34px;font-weight:400}
.charity p{width:900px;margin:8px auto 0;font-size:20px;line-height:28px;color:var(--muted)}

/* footer */
.site-footer{top:3662px;height:226px;border-top:1px solid var(--line)}
.foot-col h5{font-size:15px;font-weight:700;margin-bottom:14px}
.foot-col li{font-size:13px;list-style:none;line-height:26px;color:var(--ink)}
.foot-col li::before{content:"• ";}
.c1{left:52px;top:40px}.c2{left:330px;top:40px}.c3{left:770px;top:40px}.c4{left:1013px;top:40px}
.dot-icon{display:inline-block;width:12px;height:12px;border-radius:50%;background:var(--ink);vertical-align:middle}
.newsletter p{font-size:13px;margin-bottom:14px}
.subscribe{display:flex}
.subscribe span{width:192px;height:28px;background:#ddd;border-radius:14px 0 0 14px}
.subscribe b{height:28px;background:var(--green);color:var(--white);font-size:11px;padding:7px 12px;border-radius:0 14px 14px 0;font-weight:600}
.copyright{top:182px;width:100%;text-align:center;font-size:13px;border-top:1px solid var(--line);padding-top:14px}
</style>
</head>
<body>

<header class="site-header">
  <div class="abs brand"><span class="brand-mark"></span><span class="brand-name">Corvantis Portal</span></div>
  <div class="abs sign-in">
    <svg width="18" height="18" viewBox="0 0 18 18"><circle cx="9" cy="5" r="4" fill="#2b9be8"/><path d="M1 18c0-5 4-7 8-7s8 2 8 7z" fill="#2b9be8"/></svg>
    Sign in
  </div>
</header>

<section class="hero" role="img" aria-label="Close-up photograph of a pair of eyes behind a video player">
  <svg class="abs hero-play" viewBox="0 0 94 94"><circle cx="47" cy="47" r="44" fill="none" stroke="rgba(255,255,255,.35)" stroke-width="4"/><path d="M38 30 L64 47 L38 64 Z" fill="rgba(255,255,255,.35)"/></svg>
  <h1 class="abs hero-title">Learn faster and smarter</h1>
  <p class="abs hero-text">Corvantis Portal helps undergraduates and healthcare professionals to learn or update their knowledge about the clinically relevant anatomy, ophthalmic examination techniques and common eye disorders of the human eye.</p>
  <div class="abs hero-actions"><span class="btn btn-blue">Undergraduates</span><span class="btn btn-green">Healthcare Professionals</span></div>
</section>

<section class="trusted">
  <div class="abs trusted-rule" style="left:34px"></div>
  <div class="abs trusted-rule" style="left:736px"></div>
  <h2 class="abs trusted-title">Trusted Across The World</h2>
  <div class="abs partner-row">
    <div class="partner"><span></span></div><div class="partner"><span></span></div><div class="partner"><span></span></div>
    <div class="partner"><span></span></div><div class="partner"><span></span></div><div class="partner"><span></span></div>
  </div>
</section>

<section class="why">
  <h2 class="abs section-title">Why Corvantis Portal ?</h2>
  <div class="abs feature feature-credible">
    <h3>Credible</h3>
    <p>Written and illustrated by experienced Consultant Ophthalmologists</p>
    <ul><li>Concise text and structured content</li><li>Practical clinical emphasis</li><li>Each core topic distilled to the essential learning points</li></ul>
  </div>
  <div class="abs photo-eye" role="img" aria-label="Close-up photograph of a brown eye"></div>
  <div class="abs photo-drops" role="img" aria-label="Illustration of eye drops being applied to an eye"></div>
  <div class="abs feature feature-visual">
    <h3>Visual</h3>
    <p>Over 70 stunning 3D animations</p>
    <ul><li>Show movement around and inside the eye</li><li>Help bring key concepts to life</li><li>Lorem ipsum</li></ul>
  </div>
</section>

<section class="modules">
  <h2 class="abs section-title">Training modules</h2>
  <article class="abs module m1"><div class="module-img" role="img" aria-label="Photograph of a patient during an eye examination"></div><div class="module-body"><h4>Core Principles</h4><p>Covers clinically relevant anatomy, fundamental topics and examination techniques in Ophthalmology. [...]</p><span class="read-more">Read More ➞</span></div></article>
  <article class="abs module m2"><div class="module-img" role="img" aria-label="Photograph of a red, irritated eye"></div><div class="module-body"><h4>Ophthalmology in Practice</h4><p>Deals with common eye disorders regularly encountered by healthcare professionals hg jui tifgty [...]</p><span class="read-more">Read More ➞</span></div></article>
  <article class="abs module m3"><div class="module-img" role="img" aria-label="Photograph of a patient's eyes"></div><div class="module-body"><h4>AN Other</h4><p>Lorem ipsum dolor Fusce varius euismod lacus eget feugiat lorem ipsum dolor consectetur Fusce varius [...]</p><span class="read-more">Read More ➞</span></div></article>
</section>

<section class="team">
  <h2 class="abs section-title">Meet the team</h2>
  <div class="abs member t1"><div class="member-photo" role="img" aria-label="Portrait photograph of a doctor"></div><h4>DALTON CREWE</h4><p>Consultant Ophthalmologist</p></div>
  <div class="abs member t2"><div class="member-photo" role="img" aria-label="Portrait photograph of a doctor"></div><h4>MARISA VELDEN</h4><p>Consultant Ophthalmologist</p></div>
  <div class="abs member t3"><div class="member-photo" role="img" aria-label="Portrait photograph of a team member"></div><h4>OWEN LARKBY</h4><p>CTO</p></div>
</section>

<section class="testimonials">
  <h2 class="abs section-title">What are people saying about Corvantis Portal ?</h2>
  <div class="abs quote-photo" role="img" aria-label="Portrait photograph of the reviewer"></div>
  <div class="abs quote">
    <h4>Mr Adrian Pellow MB ChB FRCOphth</h4>
    <h5>Consultant Ophthalmologist and Head of the School of Ophthalmology, Westmoor Deanery HEW</h5>
    <p>What sets this website apart are the superb 3D animations which enhance the accompanying text more effectively than clinical videos or photographs. I would whole heartedly recommend it to medical students, optometrists, GP's, casualty doctors and ophthalmic nurse practitioners, both as an introduction to ophthalmology, but also to refresh their knowledge of core ophthalmic examination techniques and conditions.</p>
  </div>
  <div class="abs dots"><span></span><span class="on"></span><span></span></div>
</section>

<section class="cta">
  <h2>Want to try Corvantis Portal for free?</h2>
  <p>No credit card details required. It's completely free for 7 days</p>
  <span class="btn-ghost">Start Free Trial</span>
</section>

<section class="charity">
  <h2>We give 10% of our profits to charity</h2>
  <p>We believe it is important to give something back so from 2018 we will donate 10% of every subscription to a selected charity somewhere in the world which works to help prevent sight loss and treat eye diseases.</p>
</section>

<footer class="site-footer">
  <div class="abs foot-col c1"><h5>COMMUNITY</h5><ul><li><span class="dot-icon"></span></li><li><span class="dot-icon"></span></li><li><span class="dot-icon"></span></li></ul></div>
  <div class="abs foot-col c2 newsletter"><h5>NEWSLETTER</h5><p>Subscribe to our newsletter</p><div class="subscribe"><span></span><b>SUBSCRIBE</b></div></div>
  <div class="abs foot-col c3"><h5>COMPANY</h5><ul><li>About</li><li>Blog</li></ul></div>
  <div class="abs foot-col c4"><h5>POLICIES</h5><ul><li>Terms of Use</li><li>Privacy and Cookies</li></ul></div>
  <div class="abs copyright">© copyright 2018 . All Rights Reserved.</div>
</footer>

</body>
</html>
```